Salon website

Need a web design for a new blow dry and hair extension boutique in CT
would like the color scheme to be gray, white and tiffany blue
Create a web site with about 4 pages showing
1 about us page
1 blow dry services page
1 hair extension services page
1 contact us page
1 membership page
1 parties page

Industry/Entity Type

Boutique

Colors
86cfc6
cfeae6
33b7a4
aaaaaa
cbcbcb
ffffff

```html
<!DOCTYPE html>
<html lang="en">
<head>
<meta charset="utf-8">
<title>Seabreeze Blow Bar</title>
<link href="https://fonts.googleapis.com/css2?family=Open+Sans:wght@400;600;700&family=Oswald:wght@400;500&display=swap" rel="stylesheet">
<style>
:root{
  --tiffany:#86cfc6;
  --tiffany-pale:#cfeae6;
  --tiffany-deep:#33b7a4;
  --gray:#aaaaaa;
  --gray-light:#cbcbcb;
  --white:#ffffff;
  --ink:#555555;
  --footer:#5a5a5a;
  --footer-deep:#474747;
  --accent:#e8883a;
}
*{margin:0;padding:0;box-sizing:border-box}
html,body{width:900px;height:1200px;overflow:hidden}
body{font-family:"Open Sans",Arial,sans-serif;color:var(--ink);background:var(--white);position:relative;font-size:10px}
.heading{font-family:"Oswald",Arial,sans-serif;font-weight:400;color:var(--tiffany-deep);text-transform:uppercase;letter-spacing:.5px}

/* header */
.site-header{position:absolute;top:0;left:0;width:900px;height:40px;background:#f2f2f2;border-bottom:1px solid var(--gray-light)}
.main-nav{position:absolute;right:36px;top:0;display:flex}
.main-nav a{display:block;height:40px;line-height:40px;padding:0 16px;font-size:10px;text-transform:uppercase;color:#777;text-decoration:none}
.main-nav a.active{background:var(--gray);color:var(--white)}

/* hero */
.hero{position:absolute;top:40px;left:0;width:900px;height:410px;background:radial-gradient(ellipse at 50% 45%,#d9d9d9 0%,#c4c4c4 45%,#a9a9a9 100%)}
.brand{position:absolute;top:0;left:36px;width:150px;background:var(--white);box-shadow:0 1px 3px rgba(0,0,0,.15)}
.brand-name{display:flex;align-items:center;gap:6px;height:52px;padding:0 12px;font-family:"Open Sans",sans-serif;font-weight:600;font-size:13px;color:var(--tiffany-deep)}
.brand-name .dot{width:10px;height:10px;border-radius:50%;background:var(--tiffany)}
.brand-phone{background:var(--tiffany-deep);color:var(--white);font-size:10px;padding:6px 12px;display:flex;align-items:center;gap:6px}
.hero-follow{position:absolute;top:38px;right:36px;background:rgba(255,255,255,.85);padding:5px 10px;font-size:9px;color:#777;display:flex;align-items:center;gap:6px}
.hero-follow span.sq{width:10px;height:10px;background:var(--tiffany-deep)}
.hero-dots{position:absolute;bottom:12px;left:50%;transform:translateX(-50%);display:flex;gap:8px}
.hero-dots i{width:7px;height:7px;border-radius:50%;background:var(--white);opacity:.6}
.hero-dots i.on{opacity:1;background:var(--tiffany-deep)}

/* services */
.services{position:absolute;top:475px;left:45px;width:560px}
.services .heading{font-size:17px;border-bottom:1px solid var(--gray-light);padding-bottom:6px;margin-bottom:14px}
.service-grid{display:grid;grid-template-columns:1fr 1fr;gap:14px 20px}
.service-card{display:flex;gap:10px;background:#f6f6f6;border:1px solid #e6e6e6;height:62px}
.service-photo{width:70px;height:60px;flex:none;background:linear-gradient(135deg,#8a7060,#c9b3a3)}
.service-card h3{font-size:9px;font-weight:700;text-transform:uppercase;color:#444;margin:7px 0 3px}
.service-card p{font-size:8px;line-height:1.35;color:#777;padding-right:8px}

.wedding{position:absolute;top:475px;left:650px;width:205px}
.wedding .heading{font-size:17px;color:var(--tiffany);margin-bottom:14px;text-align:right}
.wedding-photo{width:205px;height:110px;background:linear-gradient(135deg,#6b4a35,#b58a66 60%,#d8c2ad)}
.wedding p{font-size:8px;line-height:1.4;color:#777;margin-top:8px}

/* band */
.promo-band{position:absolute;top:685px;left:0;width:900px;height:170px;background:var(--tiffany);text-align:center;padding:22px 60px 0}
.promo-band h2{font-family:"Open Sans",sans-serif;font-weight:400;font-size:27px;line-height:1.25;color:var(--white)}
.promo-band h2 b{font-weight:600;color:#2a8f82;text-transform:uppercase}
.promo-band p{font-size:8.5px;line-height:1.5;color:var(--white);margin-top:10px;opacity:.9}

/* experts */
.experts{position:absolute;top:855px;left:45px;width:810px;display:grid;grid-template-columns:repeat(3,1fr);gap:30px;padding-top:22px}
.expert-head{display:flex;align-items:center;gap:10px}
.expert-photo{width:56px;height:56px;border-radius:50%;flex:none;background:linear-gradient(135deg,#7d5e4b,#cfb29b)}
.expert-head h3{font-family:"Oswald",sans-serif;font-weight:400;font-size:17px;color:var(--tiffany-deep);text-transform:uppercase;line-height:1}
.expert-head small{display:block;font-size:8px;color:#999;margin-top:3px}
.expert p{font-size:8px;line-height:1.4;color:#777;margin:8px 0 8px}
.btn{display:block;width:80px;margin:0 auto;background:var(--tiffany);color:var(--white);font-size:8px;text-transform:uppercase;text-align:center;padding:5px 0;border-radius:10px}

/* footer */
.site-footer{position:absolute;top:1015px;left:0;width:900px;height:170px;background:var(--footer);display:grid;grid-template-columns:repeat(4,1fr);gap:24px;padding:18px 45px 0;color:#ddd}
.site-footer h4{font-size:10px;font-weight:600;text-transform:uppercase;color:var(--tiffany);margin-bottom:10px;letter-spacing:.5px}
.site-footer p{font-size:8px;line-height:1.5;color:#ccc}
.social-row{display:flex;gap:6px;margin-bottom:10px}
.social-row span{width:18px;height:18px;background:var(--accent);border-radius:2px}
.quote{position:relative;padding:0 14px}
.quote svg{position:absolute}
.contact-line{display:flex;align-items:center;gap:5px;margin-bottom:4px;font-size:8px;color:#ccc}
.copyright{position:absolute;top:1185px;left:0;width:900px;height:15px;background:var(--footer-deep);color:#aaa;font-size:7px;line-height:15px;padding-left:45px}
</style>
</head>
<body>

<header class="site-header">
  <nav class="main-nav">
    <a class="active">Home</a><a>About Us</a><a>Services</a><a>Membership</a><a>Parties</a><a>Contact</a>
  </nav>
</header>

<section class="hero" role="img" aria-label="Portrait photo of a man with a styled haircut in a dark suit">
  <div class="brand">
    <div class="brand-name"><span class="dot"></span>Seabreeze Blow Bar</div>
    <div class="brand-phone">
      <svg width="9" height="9" viewBox="0 0 24 24"><path fill="#fff" d="M6.6 10.8a15 15 0 006.6 6.6l2.2-2.2a1 1 0 011-.25 11.4 11.4 0 003.6.57 1 1 0 011 1V20a1 1 0 01-1 1A17 17 0 013 4a1 1 0 011-1h3.5a1 1 0 011 1c0 1.25.2 2.45.57 3.6a1 1 0 01-.25 1z"/></svg>
      +1 (203) 555-0147
    </div>
  </div>
  <div class="hero-follow">Follow us <span class="sq"></span><span class="sq"></span><span class="sq"></span></div>
  <div class="hero-dots"><i></i><i class="on"></i><i></i><i></i></div>
</section>

<section class="services">
  <h2 class="heading">Our Services</h2>
  <div class="service-grid">
    <article class="service-card">
      <div class="service-photo" role="img" aria-label="Photo of a blow dry styling"></div>
      <div><h3>Blow Dry</h3><p>Smooth, bouncy blowouts styled to last for days with our signature finish.</p></div>
    </article>
    <article class="service-card">
      <div class="service-photo" role="img" aria-label="Photo of hair coloring"></div>
      <div><h3>Hair Color</h3><p>Rich, glossy color and soft highlights tailored to your tone and style.</p></div>
    </article>
    <article class="service-card">
      <div class="service-photo" role="img" aria-label="Photo of a hair spa treatment"></div>
      <div><h3>Hair Spa</h3><p>Deep conditioning treatments that restore shine, strength and softness.</p></div>
    </article>
    <article class="service-card">
      <div class="service-photo" role="img" aria-label="Photo of hair extensions"></div>
      <div><h3>Hair Extensions</h3><p>Natural looking length and volume, seamlessly blended by our experts.</p></div>
    </article>
  </div>
</section>

<aside class="wedding">
  <h2 class="heading">Wedding Style</h2>
  <div class="wedding-photo" role="img" aria-label="Photo of a braided bridal updo"></div>
  <p>Elegant updos and soft waves for brides and bridal parties, styled on site or in our boutique.</p>
</aside>

<section class="promo-band">
  <h2>Lorem ipsum dolor sit amet, <b>consectetur</b> adipisicing elit, sed incididunt ut <b>labore</b> et dolore magna aliqua. Ut enim ad <b>minim veniam</b>.</h2>
  <p>Book a blowout, treat yourself to extensions or plan a styling party with friends. Our team of stylists brings calm, care and polish to every visit, so you leave feeling fresh, confident and ready for anything the day brings.</p>
</section>

<section class="experts">
  <article class="expert">
    <div class="expert-head"><div class="expert-photo" role="img" aria-label="Photo of a stylist at work"></div><div><h3>Expert Hair Care</h3><small>Trusted stylists</small></div></div>
    <p>Our stylists are trained in the latest techniques to keep your hair healthy and beautiful.</p>
    <span class="btn">Read More</span>
  </article>
  <article class="expert">
    <div class="expert-head"><div class="expert-photo" role="img" aria-label="Photo of a styled hairdo"></div><div><h3>Expert Hair Care</h3><small>Premium products</small></div></div>
    <p>We use gentle, salon grade products chosen for lasting shine and everyday protection.</p>
    <span class="btn">Read More</span>
  </article>
  <article class="expert">
    <div class="expert-head"><div class="expert-photo" role="img" aria-label="Photo of a finished blowout"></div><div><h3>Expert Hair Care</h3><small>Relaxed boutique</small></div></div>
    <p>Unwind in a bright, welcoming space while we create the look you have in mind.</p>
    <span class="btn">Read More</span>
  </article>
</section>

<footer class="site-footer">
  <div>
    <h4>Follow Us</h4>
    <div class="social-row"><span></span><span></span><span></span></div>
    <p>Seabreeze Blow Bar<br>48 Harbor Lane<br>Mystic, CT</p>
  </div>
  <div>
    <h4>Information</h4>
    <p>Open Tuesday to Sunday with early and late appointments. Memberships, gift cards and private parties are available.</p>
  </div>
  <div>
    <h4>Testimonials</h4>
    <div class="quote">
      <svg style="left:0;top:0" width="10" height="8" viewBox="0 0 10 8"><path fill="#86cfc6" d="M0 8V4L2 0h2L3 4h1v4zM6 8V4L8 0h2L9 4h1v4z"/></svg>
      <p>The best blowout I have ever had. Friendly team, lovely space and hair that lasted all week.</p>
      <svg style="right:0;bottom:-8px" width="10" height="8" viewBox="0 0 10 8"><path fill="#86cfc6" d="M10 0v4L8 8H6l1-4H6V0zM4 0v4L2 8H0l1-4H0V0z"/></svg>
    </div>
  </div>
  <div>
    <h4>Contact Us</h4>
    <div class="contact-line"><svg width="8" height="10" viewBox="0 0 8 10"><path fill="#86cfc6" d="M4 0a4 4 0 014 4c0 3-4 6-4 6S0 7 0 4a4 4 0 014-4zm0 2.5a1.5 1.5 0 100 3 1.5 1.5 0 000-3z"/></svg>48 Harbor Lane, Mystic, CT</div>
    <div class="contact-line"><svg width="9" height="9" viewBox="0 0 24 24"><path fill="#86cfc6" d="M6.6 10.8a15 15 0 006.6 6.6l2.2-2.2a1 1 0 011-.25 11.4 11.4 0 003.6.57 1 1 0 011 1V20a1 1 0 01-1 1A17 17 0 013 4a1 1 0 011-1h3.5a1 1 0 011 1c0 1.25.2 2.45.57 3.6a1 1 0 01-.25 1z"/></svg>+1 (203) 555-0147</div>
    <div class="contact-line"><svg width="10" height="8" viewBox="0 0 10 8"><rect x=".5" y=".5" width="9" height="7" fill="none" stroke="#86cfc6"/><path d="M.5.5L5 4.5 9.5.5" fill="none" stroke="#86cfc6"/></svg>hello@seabreezeblowbar.com</div>
  </div>
</footer>
<div class="copyright">Copyright &copy; Seabreeze Blow Bar. All rights reserved.</div>

</body>
</html>
```